Plakat für Hausverwaltung
Zielgruppe
Hausverwaltung
(Verwaltung von Wohn- und Gewerbeimmobilien)
Aufgabenstellung
Es soll ein Werbeplakat werden, Die Inhalte der Dienstleistung und die Firmenfarben kann der Webseite entnommen werden.
Ein guter Werbespruch und ansprechendes Desing ohne viel Schrift.

```html
<!DOCTYPE html>
<html lang="de">
<head>
<meta charset="utf-8">
<title>KVR Hausverwaltung – Banner</title>
<link href="https://fonts.googleapis.com/css2?family=Roboto:wght@400;500;700;900&display=swap" rel="stylesheet">
<style>
  :root {
    --page-bg: #e4e4e4;
    --sand: #d5cab3;
    --ink: #262626;
    --charcoal: #3a3a3c;
    --sky: #5aaed3;
    --sand-light: #ddd3c0;
    --photo-top: #c9cdd2;
    --photo-bottom: #8b8f95;
  }
  * { box-sizing: border-box; margin: 0; padding: 0; }
  html, body {
    width: 1200px; height: 780px; overflow: hidden;
    background: var(--page-bg);
    font-family: "Roboto", Arial, sans-serif;
  }
  .banner {
    position: absolute; left: 20px; top: 100px;
    width: 1160px; height: 580px;
    background: var(--sand);
    overflow: hidden;
    box-shadow: 0 6px 18px rgba(0,0,0,.18);
  }
  .team-photo {
    position: absolute; inset: 0 0 100px 0;
  }
  .brand {
    position: absolute; left: 66px; top: 58px;
    color: var(--ink);
  }
  .brand-row { display: flex; align-items: center; gap: 14px; margin-left: 106px; }
  .brand-name {
    font-size: 38px; font-weight: 500; letter-spacing: 14px;
  }
  .brand-mark { width: 30px; height: 30px; border: 2px solid var(--ink); }
  .brand-descriptor {
    margin-top: 8px; font-size: 17px; font-weight: 500; letter-spacing: .2px;
  }
  .headline {
    position: absolute; left: 64px; top: 190px;
    font-size: 52px; font-weight: 900; line-height: 66px;
    letter-spacing: 2px; color: var(--ink);
  }
  .headline .city {
    position: relative; display: inline-block;
  }
  .headline .city::after {
    content: ""; position: absolute; left: 0; right: 16px; bottom: -4px;
    height: 6px; background: var(--sky);
  }
  .services {
    position: absolute; left: 66px; top: 348px;
    font-size: 22px; font-weight: 500; line-height: 40px;
    letter-spacing: 1.2px; color: var(--ink);
  }
  .footer-band {
    position: absolute; left: 0; right: 0; bottom: 0; height: 100px;
    background: var(--charcoal);
    border-top: 8px solid var(--sky);
    display: flex; align-items: center; justify-content: space-between;
    padding: 0 48px 0 66px;
  }
  .claim {
    color: var(--sky); font-size: 26px; font-weight: 700; letter-spacing: 1.8px;
    margin-top: 22px;
  }
  .website {
    color: var(--sand-light); font-size: 31px; font-weight: 700; letter-spacing: 1.6px;
    margin-top: -22px;
  }
</style>
</head>
<body>
  <section class="banner">
    <svg class="team-photo" width="1160" height="480" viewBox="0 0 1160 480" role="img" aria-label="Foto: drei Mitarbeitende des Teams vor einem Regal mit Aktenordnern">
      <defs>
        <linearGradient id="photoTone" x1="0" y1="0" x2="0" y2="1">
          <stop offset="0" stop-color="var(--photo-top)"/>
          <stop offset="1" stop-color="var(--photo-bottom)"/>
        </linearGradient>
      </defs>
      <polygon points="789,0 1160,0 1160,480 626,480" fill="url(#photoTone)"/>
    </svg>

    <div class="brand">
      <div class="brand-row">
        <span class="brand-name">KVR</span>
        <span class="brand-mark"></span>
      </div>
      <div class="brand-descriptor">Haus- und Grundstücksverwaltungs GmbH</div>
    </div>

    <h1 class="headline">IHRE HAUSVERWALTUNG<br>IN UND UM <span class="city">MARBURG!</span></h1>

    <p class="services">Verwaltung von Wohnungseigentümer-<br>gemeinschaften und Miethäusern</p>

    <div class="footer-band">
      <span class="claim">Vertrauen Sie 25 Jahren fachkundiger Erfahrung!</span>
      <span class="website">www.kvr-marburg.de</span>
    </div>
  </section>
</body>
</html>
```